Building Company Business Card Design

Need a design for a business card:
It needs to have: Name, Phone, Facebook link, Website, email
i would also like a list of works we undertake:
-New Homes
-Extensions, Renovations & Bathrooms
-Decking, Carports, Sheds (Residential and Industrial)
-Carpentry
-Fences, Patios & Pergolas

Name, Phone, Facebook link, Website, email + details of services provided listed in description

```html
<!DOCTYPE html>
<html lang="en">
<head>
<meta charset="utf-8">
<title>Ridgeline Homes – Business Card</title>
<link rel="stylesheet" href="https://fonts.googleapis.com/css2?family=Arimo:wght@400;700&display=swap">
<style>
  :root {
    --green: #1f9e48;
    --green-text: #22a24a;
    --ink: #222222;
    --grey: #555555;
    --rule: #8a8a8a;
    --paper: #f6f6f6;
    --backdrop: #dcdcdc;
  }
  html, body {
    margin: 0;
    padding: 0;
    overflow: hidden;
  }
  body {
    width: 1200px;
    height: 1040px;
    background: var(--backdrop);
    font-family: "Arimo", Arial, sans-serif;
    position: relative;
  }
  .card {
    position: absolute;
    left: 280px;
    width: 640px;
    height: 366px;
    border-radius: 18px;
    overflow: hidden;
    box-shadow: 0 3px 6px rgba(0,0,0,0.25);
  }
  /* Front */
  .card-front {
    top: 130px;
    background: var(--paper);
  }
  .brand {
    position: absolute;
    text-align: center;
    color: var(--ink);
    font-weight: 700;
    line-height: 1;
    display: flex;
    align-items: center;
    gap: 10px;
  }
  .brand .mark {
    width: 12px;
    height: 12px;
    background: var(--green);
    flex: none;
  }
  .brand-front {
    left: 66px;
    top: 180px;
  }
  .brand-front .brand-name { font-size: 25px; letter-spacing: 0.3px; }
  .brand-front .brand-sub { font-size: 12.5px; letter-spacing: 0.4px; margin-top: 3px; }
  .divider {
    position: absolute;
    left: 354px;
    top: 110px;
    width: 1px;
    height: 146px;
    background: #bdbdbd;
  }
  .person {
    position: absolute;
    left: 373px;
    top: 108px;
  }
  .person-name {
    font-size: 24px;
    font-weight: 700;
    color: var(--green-text);
    margin: 0;
  }
  .person-role {
    font-size: 16.5px;
    color: var(--grey);
    margin: 2px 0 0 2px;
  }
  .contacts {
    position: absolute;
    left: 374px;
    top: 176px;
    margin: 0;
    padding: 0;
    list-style: none;
    font-size: 16px;
    color: var(--ink);
  }
  .contacts li {
    display: flex;
    align-items: center;
    gap: 8px;
    height: 19.2px;
  }
  .contacts svg { width: 13px; height: 13px; flex: none; }
  .front-rule {
    position: absolute;
    left: 0; right: 0;
    top: 344px;
    height: 3px;
    background: var(--rule);
  }
  .front-band {
    position: absolute;
    left: 0; right: 0;
    top: 348px;
    bottom: 0;
    background: var(--green);
  }
  /* Back */
  .card-back {
    top: 570px;
    background: var(--green);
    color: #ffffff;
  }
  .brand-back {
    left: 0; right: 0;
    top: 140px;
    flex-direction: column;
    color: #ffffff;
    gap: 0;
  }
  .brand-back .brand-name { font-size: 46px; letter-spacing: 0.5px; }
  .brand-back .brand-sub { font-size: 23px; letter-spacing: 0.6px; margin-top: 6px; }
  .services {
    position: absolute;
    left: 0; right: 0;
    top: 276px;
    margin: 0;
    text-align: center;
    font-size: 16px;
    line-height: 19px;
  }
  .services .dot {
    display: inline-block;
    width: 5px;
    height: 5px;
    background: #ffffff;
    margin: 0 10px;
    vertical-align: middle;
  }
</style>
</head>
<body>

<section class="card card-front" aria-label="Business card front">
  <div class="brand brand-front">
    <span class="mark"></span>
    <div>
      <div class="brand-name">RIDGELINE HOMES</div>
      <div class="brand-sub">AND DEVELOPMENTS PTY LTD</div>
    </div>
  </div>

  <div class="divider"></div>

  <div class="person">
    <p class="person-name">Thomas Avery</p>
    <p class="person-role">President</p>
  </div>

  <ul class="contacts">
    <li>
      <svg viewBox="0 0 16 16" aria-hidden="true"><path fill="#22a24a" d="M3.6 1.2l2.3 2.8-1.3 1.7c.9 2 2.5 3.6 4.5 4.6l1.7-1.3 2.8 2.3-1.2 2.4C7.3 13.3 2.7 8.7 1.2 3.6z"/></svg>
      <span>(612) 5550-1874</span>
    </li>
    <li>
      <svg viewBox="0 0 16 16" aria-hidden="true"><rect x="1" y="4" width="14" height="9" fill="#22a24a"/><path d="M1.5 4.5L8 9.5l6.5-5" stroke="#fff" stroke-width="1.3" fill="none"/></svg>
      <span>info@ridgelinehomes.com</span>
    </li>
    <li>
      <svg viewBox="0 0 16 16" aria-hidden="true"><circle cx="8" cy="8" r="7" fill="#22a24a"/><path d="M1.5 8h13M8 1v14M8 1c-3 3.5-3 10.5 0 14M8 1c3 3.5 3 10.5 0 14" stroke="#fff" stroke-width="1" fill="none"/></svg>
      <span>www.ridgelinehomes.com</span>
    </li>
    <li>
      <svg viewBox="0 0 16 16" aria-hidden="true"><circle cx="8" cy="8" r="7" fill="#22a24a"/></svg>
      <span>@ridgelinehomes</span>
    </li>
  </ul>

  <div class="front-rule"></div>
  <div class="front-band"></div>
</section>

<section class="card card-back" aria-label="Business card back">
  <div class="brand brand-back">
    <div class="brand-name">RIDGELINE HOMES</div>
    <div class="brand-sub">AND DEVELOPMENTS PTY LTD</div>
  </div>

  <p class="services">
    New Homes<span class="dot"></span>Extensions, Renovations &amp; Bathrooms<br>
    Decking, Carports, Sheds (Residential and Industrial)<br>
    Carpentry<span class="dot"></span>Fences, Patios &amp; Pergolas
  </p>
</section>

</body>
</html>
```